Varden Ridge Concrete Pumping needs a logo design and is in the concrete industry

A creative design for this Varden Ridge Concrete Pumping business. Using a trailer mounted line pump, not a boom pump.
Colour to be used is orange and a mix of white or black writing.
Target Market(s)
General Public, anyone
Industry/Entity Type
Concrete
Contact Information for Business Card
Varden Ridge Concrete Pumping
Brennan Holloway
PO BOX 47
Kelvale VIC 3391
Phone: 0491552083
Email: Holloway@postwren.com.au
Colors
f37122
000000
ffffff
Requirements
Must have
- Details listed
Nice to have
- A great logo
Should not have
- anything silly

```html
<!DOCTYPE html>
<html lang="en">
<head>
<meta charset="utf-8">
<title>Varden Ridge Concrete Pumping – Business Card</title>
<link rel="stylesheet" href="https://fonts.googleapis.com/css2?family=Source+Sans+3:wght@400;600;700&display=swap">
<style>
  :root {
    --orange: #f37122;
    --black: #000000;
    --white: #ffffff;
    --tab-grey: #bdbdbd;
    --stage: #3b3531;
  }
  * { box-sizing: border-box; margin: 0; padding: 0; }
  html, body {
    width: 1200px;
    height: 844px;
    overflow: hidden;
    background: var(--stage);
    font-family: "Source Sans 3", "Helvetica Neue", Arial, sans-serif;
  }
  .canvas {
    position: relative;
    width: 1200px;
    height: 844px;
  }
  .card {
    position: absolute;
    top: 272px;
    width: 520px;
    height: 300px;
    overflow: hidden;
    box-shadow: 0 10px 28px rgba(0,0,0,0.45);
  }

  /* Contact side */
  .card--contact {
    left: 60px;
    background: linear-gradient(100deg, #000 0%, #0b0b0b 55%, #1d1d1d 100%);
  }
  .band {
    position: absolute;
    left: 0;
    width: 100%;
    height: 11px;
    background: var(--orange);
  }
  .band--top { top: 0; }
  .band--bottom { bottom: 14px; }
  .person {
    position: absolute;
    left: 140px;
    top: 58px;
    text-align: center;
  }
  .person__name {
    color: var(--orange);
    font-weight: 700;
    font-size: 15px;
    letter-spacing: 0.3px;
    padding: 0 4px 2px;
    border-bottom: 1px solid var(--orange);
  }
  .person__role {
    color: var(--white);
    font-size: 12px;
    margin-top: 2px;
  }
  .contact {
    position: absolute;
    left: 0;
    width: 100%;
    top: 160px;
    text-align: center;
    color: var(--white);
    font-size: 14px;
    line-height: 18px;
  }
  .contact__address {
    margin-top: 12px;
    font-size: 15px;
  }

  /* Brand side */
  .card--brand {
    left: 620px;
    background: radial-gradient(ellipse at 48% 42%, #2a2a2a 0%, #0c0c0c 45%, #000 80%);
  }
  .tab {
    position: absolute;
    width: 26px;
    height: 38px;
    background: var(--orange);
  }
  .tab::after {
    content: "";
    position: absolute;
    top: 0;
    width: 4px;
    height: 100%;
    background: var(--tab-grey);
  }
  .tab--right { right: 0; top: 40px; }
  .tab--right::after { right: 0; }
  .tab--left { left: 0; bottom: 48px; }
  .tab--left::after { left: 0; }
  .brand {
    position: absolute;
    left: 0;
    width: 100%;
    top: 108px;
    text-align: center;
    color: var(--orange);
    font-weight: 600;
  }
  .brand__name {
    font-size: 38px;
    line-height: 40px;
  }
  .brand__line {
    font-size: 13px;
    letter-spacing: 4.2px;
    margin-top: 4px;
  }
</style>
</head>
<body>
<main class="canvas">

  <section class="card card--contact" aria-label="Business card, contact side">
    <div class="band band--top"></div>
    <div class="person">
      <p class="person__name">BRENNAN HOLLOWAY</p>
      <p class="person__role">Managing Director</p>
    </div>
    <div class="contact">
      <p>0491552083</p>
      <p>Holloway@postwren.com.au</p>
      <p class="contact__address">PO BOX 47 | Kelvale VIC 3391</p>
    </div>
    <div class="band band--bottom"></div>
  </section>

  <section class="card card--brand" aria-label="Business card, brand side">
    <div class="tab tab--right"></div>
    <div class="brand">
      <p class="brand__name">Varden Ridge</p>
      <p class="brand__line">CONCRETE PUMPING</p>
    </div>
    <div class="tab tab--left"></div>
  </section>

</main>
</body>
</html>
```